New high end server provider needs wordpress design

www.kv7hosting.com

Need a wordpress design for a high end server provider that provides overclocked dedicated servers for rent. We are located in Chicago but we have a presence is Virginia and Nevada for both our east and west coast customers.

We are a server provider that specializes in top end hardware with every feature designed for optimum performance. If it is not the best quality part or provides the best possible performance we don't run it. Our customers are mainly those that want the best single threaded performance possible from their hardware. We would be selling our services directly on our website via WHMCS.

We would like to see designs that are very modern and simplistic yet very attractive looking and catchy. Would prefer colors in the blues and greens and white. These colors are not necessary and I would be open to another color scheme if it looks good.

The final design should show speed and performance while being simplistic and easy on the eyes.

Logo and company name added and payment changed to guaranteed.  Looking for a wordpress template with the same pages as kv7hosting.com but with a redesigned look and feel.  

WHMCS control panel design also part of the design request.

If you have any questions please let me know!  This is just for kv7hosting.com and a main page for WHMCS (no coding just design).

Target Market(s)

IT Guru's (mostly men in their 20's to 30's)

Industry/Entity Type

Hardware

Requirements
Must have
• WHMCS panel design to fit with website theme.
Nice to have
• Main slider on home page similar to one of our other websites at www.kv7hosting.com
Should not have
• Flash or frames

```html
<!DOCTYPE html>
<html lang="en">
<head>
<meta charset="utf-8">
<title>KV7 Hosting – Home</title>
<link href="https://fonts.googleapis.com/css2?family=Open+Sans:ital,wdth,wght@0,75..100,300..600;1,75..100,300..600&family=Pathway+Gothic+One&display=swap" rel="stylesheet">
<style>
:root{
  --header-bg:#2c3038;
  --nav-band:#000;
  --nav-bar:#2f2f30;
  --nav-divider:#1d1d1d;
  --nav-text:#f2f2f2;
  --accent-line:#52d39b;
  --slider-green:#d7ecd9;
  --slider-edge:#9bb9a2;
  --label-yellow:#fff200;
  --section-gray:#e4e4e4;
  --panel:#ebebeb;
  --panel-strip:#e0e1e1;
  --media-box:#60626e;
  --text-dark:#1b1b1b;
  --text-mid:#7a7a7a;
  --quote:#8b8b8b;
  --field:#2e3538;
  --field-text:#e8f5df;
  --twitter-band:#2b2b2d;
  --footer-bg:#3f4042;
  --footer-line:#8fc494;
  --footer-text:#cfcfcf;
  --social:#2d9a63;
  --link-blue:#4d6bd1;
}
*{margin:0;padding:0;box-sizing:border-box}
html,body{width:1121px;height:1200px;overflow:hidden}
body{position:relative;background:#fff;font-family:Arial,Helvetica,sans-serif}
.abs{position:absolute}

.site-header{left:0;top:0;width:1121px;height:89px;background:var(--header-bg)}
.logo{left:129px;top:14px;font-family:'Open Sans',sans-serif;font-size:52px;color:#eef0f2;letter-spacing:-1px}
.search{left:780px;top:37px;width:154px;height:24px;border-radius:12px;background:#2b2e33;border:1px solid #4a4e55;box-shadow:inset 0 1px 3px #000;color:#9a9ea4;font-size:11px;padding:5px 0 0 19px;letter-spacing:.3px}
.search svg{position:absolute;right:13px;top:4px}
.accent{left:0;top:89px;width:1121px;height:1px;background:var(--accent-line)}

.nav-band{left:0;top:90px;width:1121px;height:68px;background:var(--nav-band)}
.nav-band-inner{left:5px;top:98px;width:1109px;height:51px;background:#23272d}
.main-nav{left:129px;top:98px;width:868px;height:50px;background:linear-gradient(#3a3a3b,#2a2a2b);display:flex}
.main-nav a{display:flex;align-items:center;justify-content:center;height:50px;color:var(--nav-text);font-size:12.5px;font-weight:bold;text-decoration:none;border-right:2px solid var(--nav-divider)}
.dropdown{z-index:10;left:375px;top:148px;width:148px;height:135px;background:#2f2f30;border-radius:0 0 3px 3px;padding:8px 14px 0 14px;box-shadow:0 2px 4px rgba(0,0,0,.3)}
.dropdown li{list-style:none;height:28px;border-bottom:1px solid #1f1f1f;color:#a9a9a9;font-size:11px;line-height:28px}
.dropdown li:last-child{border:none}
.dropdown li.current{color:#f4f4f4}

.slider{left:126px;top:171px;width:883px;height:348px;border-radius:4px;background:radial-gradient(ellipse at center,#f0f8f0 0%,var(--slider-green) 65%,var(--slider-edge) 100%);box-shadow:0 1px 3px rgba(0,0,0,.4)}
.slide-notch{top:292px;width:80px;height:80px;border-radius:50%;background:#fff}
.slide-arrow{width:46px;height:46px;border-radius:50%;background:linear-gradient(#f7f7f7,#d9d9d9);box-shadow:0 1px 3px rgba(0,0,0,.35);top:309px}
.slide-arrow svg{position:absolute;left:9px;top:9px}
.slider-label{left:164px;top:463px;width:333px;height:29px;background:var(--label-yellow);font-family:'Open Sans',sans-serif;font-size:23px;color:#111;padding-left:12px;line-height:30px}

.content-band{left:0;top:558px;width:1121px;height:420px;background:var(--section-gray)}
.tab{top:567px;height:38px;border-radius:14px 14px 0 0;font-family:'Open Sans',sans-serif;font-size:16px;padding-top:13px}
.tab-company{left:109px;width:128px;background:linear-gradient(90deg,#c9c9c9 0,#ebebeb 12%);color:var(--text-dark);padding-left:25px}
.tab-reviews{left:235px;width:153px;background:linear-gradient(90deg,#ececec 80%,#bdbdbd);color:#9a9a9a;padding-left:32px}
.panel{left:91px;top:604px;width:907px;height:314px;background:var(--panel);border-radius:14px;box-shadow:0 0 30px rgba(0,0,0,.08)}
.panel-strip{left:91px;top:888px;width:907px;height:30px;background:var(--panel-strip);border-radius:0 0 14px 14px}
.media{left:103px;top:625px;width:335px;height:149px;background:var(--media-box)}
.h-small{font-family:'Open Sans',sans-serif;font-size:14px;color:var(--text-dark)}
.excerpt{left:113px;top:811px;width:320px;font-family:'Open Sans',sans-serif;font-size:12px;line-height:16px;color:var(--text-mid);white-space:nowrap}
.quote{left:499px;top:655px;width:280px;font-family:'Open Sans',sans-serif;font-style:italic;font-weight:300;font-stretch:75%;font-size:23px;line-height:35px;color:var(--quote);letter-spacing:-1.2px;white-space:nowrap}
.login-icon{width:27px;height:27px;border-radius:50%;background:radial-gradient(circle at 40% 35%,#6a6f73,#2d3134);box-shadow:0 1px 2px rgba(0,0,0,.4)}
.login-icon svg{position:absolute;left:6px;top:5px}
.field{left:811px;width:137px;height:28px;border-radius:4px;background:var(--field);box-shadow:inset 0 1px 3px #000;font-family:'Pathway Gothic One',sans-serif;font-size:14px;color:var(--field-text);padding:5px 0 0 9px}
.login-links{left:811px;top:726px;font-family:'Pathway Gothic One',sans-serif;font-size:11.5px;color:#333;word-spacing:2px}
.login-go{left:924px;top:722px;width:29px;height:29px;border-radius:50%;background:radial-gradient(circle at 40% 35%,#5b6064,#23272a);box-shadow:0 1px 2px rgba(0,0,0,.4)}

.tweet-band{left:0;top:978px;width:1121px;height:95px;background:var(--twitter-band)}
.tweet-mark{left:286px;top:1014px;width:38px;height:38px;border-radius:50%;background:#141414}
.tweet-text{left:373px;top:1019px;font-size:11px;font-style:italic;color:#a5a5a5;letter-spacing:.1px}
.tweet-text b{font-weight:normal;color:#d8d8d8}
.tweet-link{left:377px;top:1034px;font-size:12px;font-style:italic;color:var(--link-blue)}
.footer-line{left:0;top:1073px;width:1121px;height:5px;background:var(--footer-line)}
.site-footer{left:0;top:1078px;width:1121px;height:122px;background:var(--footer-bg)}
.footer-links{left:222px;top:1093px;font-family:'Open Sans',sans-serif;font-size:10px;color:var(--footer-text)}
.footer-links span{border-left:1px solid #ddd;padding:0 1px 0 2px}
.footer-links span:first-child{border:none;padding-left:0}
.footer-contact{left:602px;top:1092px;font-family:'Open Sans',sans-serif;font-size:15px;color:#8a8b8d}
.footer-contact i{font-style:normal;border-left:1px solid #ccc;margin-left:6px;padding-left:9px}
.footer-phone{left:651px;top:1114px;font-family:'Open Sans',sans-serif;font-size:12px;color:#f2f2f2}
.social{top:1091px;width:37px;height:37px;border-radius:50%;background:var(--social)}
</style>
</head>
<body>

<header class="abs site-header"></header>
<div class="abs logo">Logo</div>
<div class="abs search">enter search terms..
  <svg width="16" height="15" viewBox="0 0 16 15"><circle cx="10" cy="6" r="4.5" fill="none" stroke="#8c9096" stroke-width="1.5"/><line x1="6.7" y1="9.2" x2="2" y2="13.5" stroke="#8c9096" stroke-width="2"/></svg>
</div>
<div class="abs accent"></div>

<div class="abs nav-band"></div>
<div class="abs nav-band-inner"></div>
<nav class="abs main-nav">
  <a style="width:74px">Home</a>
  <a style="width:86px">Services</a>
  <a style="width:85px">Buy</a>
  <a style="width:100px">Our Servers&nbsp;<svg width="10" height="7" viewBox="0 0 10 7"><path d="M1 1l4 4 4-4" fill="none" stroke="#fff" stroke-width="2"/></svg></a>
  <a style="width:96px">Clients</a>
  <a style="width:85px">About us</a>
  <a style="width:90px">Testimonials</a>
  <a style="width:83px">Contact</a>
</nav>

<div class="abs slider" role="img" aria-label="Slider image showcasing dedicated server hardware"></div>
<div class="abs slide-notch" style="left:73px"></div>
<div class="abs slide-notch" style="left:982px"></div>
<div class="abs slide-arrow" style="left:89px"><svg width="28" height="28" viewBox="0 0 28 28"><path d="M22 14H8M13 8l-6 6 6 6" fill="none" stroke="#777" stroke-width="3" stroke-linecap="round"/></svg></div>
<div class="abs slide-arrow" style="left:1001px"><svg width="28" height="28" viewBox="0 0 28 28"><path d="M6 14h14M15 8l6 6-6 6" fill="none" stroke="#777" stroke-width="3" stroke-linecap="round"/></svg></div>
<div class="abs slider-label">SLIDER</div>

<ul class="abs dropdown">
  <li>Server</li><li>Server</li><li class="current">Server 2</li><li>Server</li>
</ul>

<section class="abs content-band"></section>
<div class="abs tab tab-reviews">Reviews</div>
<div class="abs tab tab-company">Company</div>
<div class="abs panel"></div>
<div class="abs panel-strip"></div>
<div class="abs media" role="img" aria-label="Company feature image"></div>
<div class="abs h-small" style="left:116px;top:784px">Lorem ipsum dolor</div>
<p class="abs excerpt">Pellentesque habitant morbi tristique<br>senectus et netus et malesuada fames<br>&nbsp;ac turpis egestas vestibulum tortor quam,<br>feugiat vitae, ultricies eget, tempor sit amet[...]</p>
<div class="abs h-small" style="left:500px;top:630px">Lorem ipsum dolor</div>
<blockquote class="abs quote">“Pellentesque habitant morbi tristique<br>senectus et netus et malesuada fames<br>&nbsp;ac turpis egestas vestibulum tortor quam,<br>feugiat vitae, ultricies eget, tempor sit amet”</blockquote>

<div class="abs login-icon" style="left:773px;top:640px"><svg width="15" height="17" viewBox="0 0 15 17"><circle cx="7.5" cy="3" r="2.3" fill="#ccc"/><path d="M4 6h7l-1 5H9l-.5 5h-2L6 11H5z" fill="#ccc"/></svg></div>
<div class="abs field" style="top:638px">USERNAME</div>
<div class="abs login-icon" style="left:773px;top:689px"><svg width="15" height="17" viewBox="0 0 15 17"><circle cx="5" cy="5" r="3.5" fill="#ccc"/><path d="M7 7l6 7" stroke="#ccc" stroke-width="2.2"/></svg></div>
<div class="abs field" style="top:689px">PASSWORD</div>
<div class="abs login-links">FORGOT PASSWORD? &nbsp;REGISTER</div>
<div class="abs login-go"><svg width="29" height="29" viewBox="0 0 29 29"><path d="M8 14.5h11M14 9l5.5 5.5L14 20" fill="none" stroke="#ddd" stroke-width="3"/></svg></div>

<section class="abs tweet-band"></section>
<svg class="abs" style="left:236px;top:1028px" width="8" height="12" viewBox="0 0 8 12"><path d="M6 1L1.5 6 6 11" fill="none" stroke="#fff" stroke-width="2"/></svg>
<div class="abs tweet-mark"></div>
<div class="abs tweet-text"><b>about an hour ago</b> On-demand, virtual data center experience, look no further.</div>
<div class="abs tweet-link">http://kvhost.link/232</div>
<svg class="abs" style="left:856px;top:1029px" width="8" height="12" viewBox="0 0 8 12"><path d="M2 1l4.5 5L2 11" fill="none" stroke="#fff" stroke-width="2"/></svg>

<div class="abs footer-line"></div>
<footer class="abs site-footer"></footer>
<div class="abs footer-links"><span>About us</span><span>Our Brands</span><span>Testimonials</span><span>Contact us</span><span>Get Listed</span><span>Sitemap</span></div>
<div class="abs footer-contact">Contact us<i>Sales Support</i></div>
<div class="abs footer-phone">(00) 5555-210-44</div>
<div class="abs social" style="left:845px"></div>
<div class="abs social" style="left:892px"></div>
<div class="abs social" style="left:939px"></div>

</body>
</html>
```